Hold Each Morning As A MOSSbright Harbour

Hello Designers! We need a captivating notebook cover design for our self-development company for people with disabilities. We help people with a diagnosis see everyday as a great adventure than something to ensure. This notebook is to capture the brightness and positivity of everyday, that your struggles are meant for you to overcome. We would like to see designs that follow with our brand (uploaded) and I've also added our logo and kind of notebook as a guide. The final design should be inviting and bright. Use the title "Keep Each Morning A Quiet Lantern". Will decide the words once the background design is finalized

Notebook Size: 8.5 x 5.75 inches
Updates

Hello Designers! I'm extending the deadline to give you an opportunity to submit different and unique designs for the MOSSbright HARBOUR Journal. I've given feedback to most of you so this is your opportunity to try something new. Looking for clean, inviting and unique designs that use the logo colour scheme (attached -- navy blue, light blue, yellow, black). Preferably front and back cover designs.

Target Market(s)

Between 25-35 years

Font styles to use
Serif
Sans Serif
Decorative
Script

Colors
0255a3
fbed22

Requirements
Must have
• -Use colour scheme as per attachment as main colours (can go beyond for contrast ex. pinks/purples/indigo/etc)
Nice to have
• Would like to see designs related to nature, art and/or graphic prints.
Should not have
• icons (no stick figures), silhouettes of people, no hands
• NO stock images

```html
<!DOCTYPE html>
<html lang="en">
<head>
<meta charset="utf-8">
<title>Keep Each Morning A Quiet Lantern – Notebook Cover</title>
<link rel="stylesheet" href="https://fonts.googleapis.com/css2?family=Patrick+Hand&display=swap">
<style>
  :root {
    --page-bg: #ffffff;
    --brand-navy: #0255a3;
    --brand-yellow: #fbed22;
    --light-blue: #5fb0e6;
    --sky-blue: #3f8fd2;
    --indigo: #5a5fb8;
    --soft-violet: #9a8fd8;
    --title-white: #ffffff;
  }
  * { margin: 0; padding: 0; box-sizing: border-box; }
  html, body {
    width: 1200px;
    height: 1200px;
    overflow: hidden;
    background: var(--page-bg);
  }
  .canvas {
    position: relative;
    width: 1200px;
    height: 1200px;
    background: var(--page-bg);
  }
  .notebook-cover {
    position: absolute;
    left: 256px;
    top: 92px;
    width: 688px;
    height: 1020px;
    overflow: hidden;
    box-shadow: 3px 4px 4px rgba(0, 0, 0, 0.35);
  }
  .cover-wash {
    position: absolute;
    inset: 0;
    background:
      radial-gradient(ellipse 240px 190px at 14% 6%, var(--soft-violet), transparent 72%),
      radial-gradient(ellipse 300px 170px at 62% 20%, var(--brand-yellow), transparent 70%),
      radial-gradient(ellipse 170px 220px at 96% 38%, var(--brand-yellow), transparent 70%),
      radial-gradient(ellipse 130px 100px at 30% 62%, var(--brand-yellow), transparent 72%),
      radial-gradient(ellipse 320px 280px at 62% 78%, var(--indigo), transparent 72%),
      radial-gradient(ellipse 260px 300px at 12% 88%, var(--brand-navy), transparent 72%),
      radial-gradient(ellipse 320px 320px at 92% 8%, var(--light-blue), transparent 72%),
      linear-gradient(160deg, var(--indigo) 0%, var(--brand-navy) 30%, var(--sky-blue) 55%, var(--brand-navy) 100%);
  }
  .cover-title {
    position: absolute;
    left: 0;
    right: 0;
    top: 334px;
    text-align: center;
    font-family: "Patrick Hand", "Comic Sans MS", sans-serif;
    font-weight: 400;
    font-size: 32px;
    line-height: 44px;
    letter-spacing: 1px;
    text-transform: uppercase;
    color: var(--title-white);
  }
  .cover-title span { display: block; }
</style>
</head>
<body>
  <main class="canvas">
    <section class="notebook-cover">
      <div class="cover-wash" role="img" aria-label="Soft watercolour wash in navy, light blue and sunny yellow tones"></div>
      <h1 class="cover-title">
        <span>Keep Each Morning</span>
        <span>A Quiet</span>
        <span>Lantern</span>
      </h1>
    </section>
  </main>
</body>
</html>
```